Structural Engineering Company needs ad for magazine

We are an engineering office for structural engineering in the entertainment industry. Our focus are concert stages, festival structures, grand stands and exhibition booths. Our customers are mainly from Europe, we realize the projects worldwide. Typical customers are designer, architects, stage builders, exhibition builder and technical service provider. We are creating structural analyses, technical consulting, technical drawings and risk assessment. We are working on mid size and major events.
Some technical notes:
- CMYK profile needed, minimum 300 dpi for raster graphic
- Our primary color is Petrol. Favourite is petrol, coral and grey (black). Please use palette shown below.
- Our font in documents is Myriad. Regular at 10 pt for text and Light at 16-24pt for titles.
- The format for the ad is 61 x 127 mm (portrait) or 185 x 46 mm (landscape). Which one is up to you.
To the content:
- For contact details we just want to provide our web address "falkowerk.de" and/or our e-mail "info@falkowerk.de"
- Attached are some Logo files and photos.
- The ad do not advertise a specific product. It is more a general advertisement for the company.
- The language for the ad should be German. Below are keywords in English and corresponding German translation. You do not need to place all Keywords, it is just a brainstorming list to help you. You are also welcome to use other text. We will help with translation, if necessary.
- we like discussing ideas to get better results, so also if you have questions, please ask.
- If you need information that we haven't thought of yet, please ask.
Our slogan (also in Germany): event meets engineering
Service Keywords EN / DE
- Structural Analysis / Statische Berechnungen
- Risk Assessment / Risikobewertungen
- Consulting & Design / Beratung & Konstruktion
Technical Keywords EN / DE
- Stage machinery / Bühnentechnik
- Scaffolding / Gerüstbau
- Exhibition Booths / Messebauten
- Tents / Zelte
- Temporary Structures / Fliegende Bauten
- Truss / Traversen
- Stages / Bühnen
- Grand Stands / Tribünen
- Leightweight Construction / Leichtbau
- Steel Construction / Stahlbau
- Amusement Rides / Fahrgeschäfte
Look and feel

```html
<!DOCTYPE html>
<html lang="de">
<head>
<meta charset="utf-8">
<title>Falkowerk Engineering – Anzeige</title>
<link href="https://fonts.googleapis.com/css2?family=Montserrat:wght@300;400;500;600&display=swap" rel="stylesheet">
<style>
  :root {
    --petrol: #1fb5c9;
    --ink: #000000;
    --white: #ffffff;
  }
  * { margin: 0; padding: 0; box-sizing: border-box; }
  html, body { width: 1200px; height: 298px; overflow: hidden; background: var(--ink); }
  .ad {
    position: relative;
    width: 1200px;
    height: 298px;
    font-family: "Montserrat", sans-serif;
    color: var(--white);
    overflow: hidden;
  }
  .stage-photo {
    position: absolute;
    left: 0; top: 0;
    width: 840px; height: 298px;
    background:
      radial-gradient(ellipse 170px 150px at 580px 120px, rgba(40,20,90,0.9), transparent 70%),
      radial-gradient(ellipse 220px 130px at 600px 275px, rgba(200,110,200,0.75), transparent 70%),
      radial-gradient(ellipse 200px 160px at 760px 130px, rgba(150,200,210,0.55), transparent 70%),
      linear-gradient(100deg, #23b2c8 0%, #2a8cb4 30%, #4b3d9a 60%, #6a3aa3 80%, #3aa7c2 100%);
  }
  .headline {
    position: absolute;
    left: 32px; top: 22px;
    font-weight: 600;
    font-size: 35.5px;
    line-height: 40.6px;
    letter-spacing: -0.4px;
  }
  .gear-icon {
    position: absolute;
    left: 40px; top: 210px;
    width: 37px; height: 37px;
  }
  .slogan {
    position: absolute;
    left: 119px; top: 258px;
    font-weight: 300;
    font-size: 18px;
  }
  .slogan-rule {
    position: absolute;
    left: 81px; top: 283px;
    width: 759px; height: 1px;
    background: var(--white);
  }
  .brand-panel {
    position: absolute;
    left: 840px; top: 0;
    width: 360px; height: 298px;
    background: var(--ink);
  }
  .brand-name {
    position: absolute;
    left: 0; right: 0; top: 168px;
    text-align: center;
    font-weight: 500;
    font-size: 34px;
    letter-spacing: 8px;
    padding-left: 8px;
    text-transform: uppercase;
  }
  .brand-sub {
    position: absolute;
    left: 0; right: 0; top: 210px;
    text-align: center;
    font-weight: 400;
    font-size: 16px;
    letter-spacing: 4px;
    padding-left: 4px;
    text-transform: uppercase;
  }
  .web {
    position: absolute;
    left: 0; right: 0; top: 260px;
    text-align: center;
    font-weight: 400;
    font-size: 15px;
  }
</style>
</head>
<body>
  <div class="ad">
    <div class="stage-photo" role="img" aria-label="Nahaufnahme eines Moving-Head-Scheinwerfers an einer Traverse in türkis-violettem Bühnenlicht"></div>

    <h1 class="headline">Fachplanungsbüro für<br>Fliegende Bauten,<br>Messebau, Theater und<br>Veranstaltungstechnik.</h1>

    <svg class="gear-icon" viewBox="0 0 40 40" fill="none" stroke="#ffffff" stroke-width="1.2" aria-hidden="true">
      <circle cx="20" cy="20" r="11"/>
      <circle cx="20" cy="20" r="5"/>
      <path d="M20 4v5M20 31v5M4 20h5M31 20h5M8.7 8.7l3.5 3.5M27.8 27.8l3.5 3.5M8.7 31.3l3.5-3.5M27.8 12.2l3.5-3.5"/>
    </svg>

    <p class="slogan">Where stages meet structure.</p>
    <div class="slogan-rule"></div>

    <div class="brand-panel">
      <div class="brand-name">Falkowerk</div>
      <div class="brand-sub">Engineering</div>
      <div class="web">www.falkowerk.de</div>
    </div>
  </div>
</body>
</html>
```